Cafe - A FRAME Design

Need to create an A frame for my café.
Logo available
Word document - has basic information we think would be good.

Name: Brovvle Café

Notes from the A-frame printers.
File Requirements
• PDF without trim, crop or registration marks
• All files to be CMYK, not RGB
• All fonts converted to outlines (paths/curves)
• Embed all images and elements
• Files to be 100% scale unless otherwise specified
• 10mm Bleed
Resolution
• Bitmap images no less than 130 DPI at full size
Pantone Colours
• If required Pantone colours must be supplied

Target Market(s)

Mainly Students - University cafe

Requirements
Must have
• Cafe name: Brovvle
Nice to have
• Might be nice to have background - that orange color same as logo - just an idea

Word document - has basic idea regarding text that should be included

```html
<!DOCTYPE html>
<html lang="en">
<head>
<meta charset="utf-8">
<title>Brovvle Café – A-Frame Sign</title>
<link rel="stylesheet" href="https://fonts.googleapis.com/css2?family=Montserrat:wght@400;500;600;700&display=swap">
<style>
  :root {
    --paper: #ffffff;
    --backdrop: #f4f4f5;
    --slate: #4a4d55;
    --ember: #d35d2a;
    --ember-soft: #dd7a4c;
    --text-dark: #4a4d55;
  }
  html, body {
    margin: 0;
    padding: 0;
    width: 1200px;
    height: 718px;
    overflow: hidden;
    background: var(--backdrop);
  }
  .canvas {
    width: 1200px;
    height: 718px;
    display: flex;
    align-items: center;
    justify-content: center;
  }
  .a-frame-sign {
    width: 470px;
    height: 672px;
    display: block;
    box-shadow: 0 0 0 1px #4a4d55;
    font-family: "Montserrat", sans-serif;
  }
  .cafe-name { font-weight: 500; fill: var(--text-dark); }
  .tagline { font-weight: 500; fill: var(--paper); }
  .ribbon { fill: var(--paper); }
  .ribbon-label { font-weight: 600; fill: var(--text-dark); }
  .ribbon-note { font-weight: 500; fill: var(--text-dark); }
  .location { font-weight: 500; fill: var(--paper); }
  .pin { fill: none; stroke: var(--paper); stroke-width: 4; }
</style>
</head>
<body>
<main class="canvas">
  <svg class="a-frame-sign" viewBox="0 0 830 1186" xmlns="http://www.w3.org/2000/svg">
    <rect class="sign-top" x="0" y="0" width="830" height="1186" fill="var(--paper)"/>

    <!-- cafe name -->
    <circle class="name-dot" cx="132" cy="258" r="20" fill="var(--ember)"/>
    <text class="cafe-name" x="445" y="282" font-size="70" text-anchor="middle">Brovvle Café</text>

    <!-- slate band -->
    <path class="slate-band" fill="var(--slate)"
      d="M0,367 Q18,437 95,437 L735,437 Q812,437 830,367 L830,1186 L0,1186 Z"/>
    <text class="tagline" x="415" y="505" font-size="39" text-anchor="middle">Your environmentally</text>
    <text class="tagline" x="415" y="551" font-size="39" text-anchor="middle">&amp; sustainability focused cafe</text>

    <!-- ember band -->
    <path class="ember-band" fill="var(--ember)"
      d="M0,500 Q22,575 105,575 L725,575 Q808,575 830,500 L830,1030 Q800,1052 700,1042 Q560,1030 470,1058 Q400,1072 320,1052 Q170,1028 40,1044 Q10,1048 0,1030 Z"/>

    <rect class="leaf-border" x="17" y="572" width="105" height="465" fill="var(--ember-soft)" opacity="0.55"
      role="img" aria-label="White leaf and swirl ornament running down the left edge"/>
    <rect class="leaf-border" x="707" y="572" width="105" height="465" fill="var(--ember-soft)" opacity="0.55"
      role="img" aria-label="White leaf and swirl ornament running down the right edge"/>

    <!-- offer ribbons -->
    <g class="offer">
      <path class="ribbon" d="M160,612 L670,612 L684,650 L670,689 L160,689 L146,650 Z"/>
      <text class="ribbon-label" x="415" y="664" font-size="42" text-anchor="middle">Specialty Coffee</text>
    </g>
    <g class="offer">
      <path class="ribbon" d="M90,717 L740,717 L754,756 L740,795 L90,795 L76,756 Z"/>
      <text class="ribbon-label" x="415" y="770" font-size="42" text-anchor="middle">Fresh Food, Pastries &amp; Drinks</text>
    </g>
    <g class="offer">
      <path class="ribbon" d="M127,822 L702,822 L716,861 L702,900 L127,900 L113,861 Z"/>
      <text x="415" y="875" text-anchor="middle">
        <tspan class="ribbon-label" font-size="42">(Vegan &amp; GF)</tspan>
        <tspan class="ribbon-note" font-size="30"> options available</tspan>
      </text>
    </g>
    <g class="offer">
      <path class="ribbon" d="M160,927 L670,927 L684,966 L670,1005 L160,1005 L146,966 Z"/>
      <text class="ribbon-label" x="415" y="980" font-size="42" text-anchor="middle">Catering Available</text>
    </g>

    <!-- location -->
    <g class="location-line">
      <path class="pin" d="M200,1150 C188,1136 178,1124 178,1110 A22,22 0 0 1 222,1110 C222,1124 212,1136 200,1150 Z"/>
      <circle class="pin" cx="200" cy="1109" r="8"/>
      <text class="location" x="240" y="1139" font-size="50">@ Building 317</text>
    </g>
  </svg>
</main>
</body>
</html>
```